Web Design Project

I work in a sign company that print banners, back light films, and vinyl lettering. We also create metal store signs that lights up. We have a laser cutter that can cut plastics and a waterjet that can cut stainless steel.
Job: Create a homepage
Requirements:
1. Keep it simple and neat, I do not want it to be messy. (Similar to this website, plover, or this http://www.markelvo.example/)
2. A navigation bar that has (Will help if you show a template for one of these links):
-Home
-Signs
-Banners
-Lettering
-Prints
-Gallery
3.Bottom of the page
-Abous us
-Shipping and Returning Policy
-Resellers
4.Other (Somewhere easy to find)
-Login
-Shopping Cart
-Upload
Updates
Nice job designers. I am currently working on the Site's logo, so I will be posting that up later.
I would like you guys to change the selection on the navigation bar.
It should only have:
Banners
Lettering
Prints
Gallery
Keep up the good work
Sorry for the bad update, the Navigation bar should have:
Home
Signs
Banners
Lettering
Prints
Gallery

```html
<!DOCTYPE html>
<html lang="en">
<head>
<meta charset="utf-8">
<title>Sign Printing Homepage</title>
<link rel="stylesheet" href="https://fonts.googleapis.com/css2?family=Open+Sans:wght@300;400;600;700&display=swap">
<style>
  :root {
    --page-bg: #ffffff;
    --logo-bg: #9a9a9a;
    --logo-text: #f2f2f2;
    --util-text: #666666;
    --util-icon: #8a8a8a;
    --nav-top: #a9a9a9;
    --nav-mid: #5d5d5d;
    --nav-bottom: #3a3a3a;
    --nav-divider: #2c2c2c;
    --nav-text: #ffffff;
    --nav-active: #a9dcff;
    --caption-bg: rgba(40, 40, 40, 0.72);
    --caption-text: #f0f0f0;
    --dot: #8c8c8c;
    --dot-active: #1b87d6;
    --card-border: #dcdcdc;
    --card-title: #1a7fc0;
    --body-text: #555555;
    --button-top: #f4f4f4;
    --button-bottom: #a9a9a9;
    --button-text: #222222;
    --footer-text: #555555;
  }
  * { box-sizing: border-box; margin: 0; padding: 0; }
  html, body { width: 1200px; height: 900px; overflow: hidden; background: var(--page-bg); }
  body { font-family: "Open Sans", sans-serif; color: var(--body-text); }
  .page { position: relative; width: 1150px; height: 860px; margin: 20px 0 0 25px; }

  .logo {
    position: absolute; left: 93px; top: 16px; width: 178px; height: 58px;
    background: var(--logo-bg); color: var(--logo-text);
    font-size: 12px; display: flex; align-items: center; justify-content: center; letter-spacing: .2px;
  }

  .utility { position: absolute; top: 10px; left: 840px; display: flex; gap: 18px; list-style: none; }
  .utility li { display: flex; flex-direction: column; align-items: center; font-size: 12px; color: var(--util-text); }
  .utility .icon { margin-top: 5px; width: 24px; height: 24px; background: var(--util-icon); border-radius: 2px; display: flex; align-items: center; justify-content: center; }

  .main-nav {
    position: absolute; left: 87px; top: 95px; width: 979px; height: 38px;
    border-radius: 8px; border: 1px solid #555;
    background: linear-gradient(to bottom, var(--nav-top), var(--nav-mid) 50%, var(--nav-bottom));
    display: flex; justify-content: flex-end; overflow: hidden;
  }
  .main-nav ul { display: flex; list-style: none; height: 100%; }
  .main-nav li {
    border-left: 1px solid var(--nav-divider); box-shadow: inset 1px 0 0 rgba(255,255,255,.25);
    display: flex; align-items: center; justify-content: center;
    color: var(--nav-text); font-weight: 700; font-size: 13px; letter-spacing: .4px;
    text-shadow: 0 1px 1px rgba(0,0,0,.6);
  }
  .main-nav li.active { color: var(--nav-active); background: rgba(255,255,255,.08); }

  .hero {
    position: absolute; left: 87px; top: 142px; width: 977px; height: 440px;
    background: linear-gradient(100deg, #3c8a6a 0%, #e9e6e0 22%, #3f6c3a 40%, #d8d3cc 55%, #2f8f7a 70%, #c6d6d8 85%, #e8eef0 100%);
    box-shadow: 0 6px 8px -6px rgba(0,0,0,.5);
  }
  .hero-caption {
    position: absolute; left: 0; bottom: 0; width: 100%; height: 66px;
    background: var(--caption-bg); color: var(--caption-text);
    font-weight: 300; font-size: 14px; line-height: 18px; padding: 10px 36px;
  }

  .slider-dots { position: absolute; left: 515px; top: 597px; display: flex; gap: 4px; list-style: none; }
  .slider-dots li { width: 15px; height: 15px; border-radius: 50%; background: var(--dot); }
  .slider-dots li.active { background: var(--dot-active); }

  .service-card {
    position: absolute; top: 633px; width: 232px; height: 165px;
    border: 1px solid var(--card-border); border-bottom: none; border-radius: 8px 8px 0 0;
  }
  .service-card h2 {
    font-weight: 400; font-size: 17px; color: var(--card-title);
    margin: 5px 6px 0; padding: 0 9px 3px; border-bottom: 1px solid var(--card-border);
  }
  .service-card .thumb {
    position: absolute; left: 8px; top: 38px; width: 90px; height: 92px;
    border: 2px solid #e6e6e6;
  }
  .service-card p { position: absolute; left: 105px; top: 38px; width: 122px; font-size: 10.5px; line-height: 13px; }
  .read-more {
    position: absolute; right: 10px; top: 135px; width: 102px; height: 24px; border-radius: 12px;
    background: linear-gradient(to bottom, var(--button-top), var(--button-bottom));
    border: 1px solid #999; box-shadow: 0 2px 2px rgba(0,0,0,.25);
    font-size: 13.5px; color: var(--button-text); display: flex; align-items: center; justify-content: center;
  }

  .site-footer {
    position: absolute; left: 290px; top: 806px; width: 580px; height: 34px;
    display: flex; align-items: center; justify-content: center; gap: 10px;
    font-size: 13px; color: var(--footer-text);
    background:
      linear-gradient(to right, transparent, rgba(0,0,0,.14) 50%, transparent) top / 100% 2px no-repeat,
      linear-gradient(to right, transparent, rgba(0,0,0,.18) 50%, transparent) bottom / 100% 3px no-repeat;
  }
</style>
</head>
<body>
<div class="page">
  <div class="logo">COMPANY LOGO</div>

  <ul class="utility">
    <li>Login
      <span class="icon"><svg width="18" height="10" viewBox="0 0 18 10"><circle cx="4" cy="5" r="3.5" fill="#fff"/><rect x="6" y="4" width="11" height="2.5" fill="#fff"/><rect x="13" y="6" width="2" height="3" fill="#fff"/></svg></span>
    </li>
    <li>Shopping Cart
      <span class="icon"><svg width="18" height="16" viewBox="0 0 18 16"><path d="M1 2h3l2 8h9l2-6H5" fill="none" stroke="#fff" stroke-width="1.6"/><circle cx="7" cy="13" r="1.6" fill="#fff"/><circle cx="14" cy="13" r="1.6" fill="#fff"/></svg></span>
    </li>
    <li>Upload
      <span class="icon"><svg width="16" height="18" viewBox="0 0 16 18"><path d="M2 7v10h12V7" fill="none" stroke="#fff" stroke-width="1.6"/><path d="M8 14V3M4 7l4-4 4 4" fill="none" stroke="#fff" stroke-width="1.6"/></svg></span>
    </li>
  </ul>

  <nav class="main-nav">
    <ul>
      <li class="active" style="width:84px">Home</li>
      <li style="width:84px">Signs</li>
      <li style="width:100px">Banners</li>
      <li style="width:108px">Lettering</li>
      <li style="width:88px">Prints</li>
      <li style="width:96px">Gallery</li>
    </ul>
  </nav>

  <section class="hero" role="img" aria-label="Photo of printed banners and posters hanging in a row at a print show">
    <p class="hero-caption">Lorem Ipsum is simply dummy text of the printing and typesetting industry. Lorem Ipsum is simply dummy text of the printing and type-setting industry.</p>
  </section>

  <ul class="slider-dots">
    <li class="active"></li><li></li><li></li><li></li><li></li>
  </ul>

  <article class="service-card" style="left:87px">
    <h2>Banner</h2>
    <div class="thumb" role="img" aria-label="Wide-format banner printer" style="background:linear-gradient(160deg,#f4f4f4,#9a9a9a 55%,#d9a040)"></div>
    <p>Lorem Ipsum is simply dummy text of the printing and typesetting industry. Lorem Ipsum is simply dummy text of the printing and type-setting industry.</p>
    <span class="read-more">Read More</span>
  </article>

  <article class="service-card" style="left:336px">
    <h2>Baklight Film</h2>
    <div class="thumb" role="img" aria-label="Illuminated backlit film displays" style="background:linear-gradient(160deg,#3a2f28,#e0b860 50%,#2b2622)"></div>
    <p>Lorem Ipsum is simply dummy text of the printing and typesetting industry. Lorem Ipsum is simply dummy text of the printing and type-setting industry.</p>
    <span class="read-more">Read More</span>
  </article>

  <article class="service-card" style="left:584px">
    <h2>Vinyl</h2>
    <div class="thumb" role="img" aria-label="Vinyl cutter printing a roll" style="background:linear-gradient(170deg,#d8d8d8,#f5f5f5 45%,#222 60%,#e0a020)"></div>
    <p>Lorem Ipsum is simply dummy text of the printing and typesetting industry. Lorem Ipsum is simply dummy text of the printing and type-setting industry.</p>
    <span class="read-more">Read More</span>
  </article>

  <article class="service-card" style="left:832px">
    <h2>PCB Poster</h2>
    <div class="thumb" role="img" aria-label="Colourful printed poster sample" style="background:linear-gradient(135deg,#e0206a,#f0c020 35%,#30b040 60%,#2060d0)"></div>
    <p>Lorem Ipsum is simply dummy text of the printing and typesetting industry. Lorem Ipsum is simply dummy text of the printing and type-setting industry.</p>
    <span class="read-more">Read More</span>
  </article>

  <footer class="site-footer">
    <span>Abous us</span><span>|</span><span>Shipping and Returning Policy</span><span>|</span><span>Resellers</span>
  </footer>
</div>
</body>
</html>
```